Law firm business cards and stationary
Traditional professional presentation
Law firm business cards and stationary - Law
Creative Brief
Use same font as used in my logo
Other traditional looking fonts will be considered
Professional
Marla J. Pettigrew
Attorney at Law
742 E. 9th Ave, Ste 114 Spokane, WA 99208
(509) TRY-CASE
barrister@mailwove.com
roadcasedefenders.org
Please see uploaded logo. The phone number (509) TRY-CASE is displayed prominently in all marketing. Thank you.

```html
<!DOCTYPE html>
<html lang="en">
<head>
<meta charset="utf-8">
<title>The Halvorsen Firm – Business Card</title>
<link rel="stylesheet" href="https://fonts.googleapis.com/css2?family=Cormorant+SC:wght@500;600&display=swap">
<style>
  :root {
    --backdrop: #e9e6e1;
    --card: #ffffff;
    --ink: #3a3a3a;
    --green: #5aa83a;
    --rule: #9fcf8a;
  }
  * { margin: 0; padding: 0; box-sizing: border-box; }
  html, body {
    width: 1200px; height: 914px; overflow: hidden;
    background: var(--backdrop);
    font-family: "Cormorant SC", "Times New Roman", serif;
    color: var(--ink);
  }
  .card {
    position: absolute;
    left: 110px; top: 172px;
    width: 980px; height: 570px;
    background: var(--card);
    box-shadow: 0 6px 24px rgba(0,0,0,0.12);
  }
  .brand {
    position: absolute;
    top: 140px; left: 0; right: 0;
    display: flex; align-items: center; justify-content: center; gap: 18px;
  }
  .brand-dot {
    width: 54px; height: 54px; border-radius: 50%;
    background: var(--green);
  }
  .brand-name {
    font-size: 50px; font-weight: 600; letter-spacing: 2px;
    color: var(--ink);
  }
  .identity {
    position: absolute; top: 272px; left: 0; right: 0;
    text-align: center;
    font-size: 28px; font-weight: 600; color: var(--green); letter-spacing: 1px;
  }
  .identity .divider { color: var(--rule); margin: 0 10px; font-weight: 500; }
  .identity .title { font-weight: 500; }
  .contacts {
    position: absolute; top: 350px; left: 92px; right: 92px;
    display: grid; grid-template-columns: 1fr 1fr; row-gap: 14px; column-gap: 30px;
    font-size: 22px; font-weight: 600;
  }
  .contact { display: flex; align-items: center; gap: 10px; white-space: nowrap; }
  .contact-group { display: flex; gap: 30px; }
  .contact-icon {
    width: 20px; height: 20px; flex: none;
  }
  .contact-right { padding-left: 40px; }
</style>
</head>
<body>
  <div class="card">
    <div class="brand">
      <span class="brand-dot"></span>
      <span class="brand-name">The Halvorsen Firm</span>
    </div>

    <p class="identity">
      Marla J. Pettigrew<span class="divider">|</span><span class="title">Attorney at Law</span>
    </p>

    <div class="contacts">
      <div class="contact">
        <svg class="contact-icon" viewBox="0 0 20 20" aria-hidden="true">
          <circle cx="10" cy="10" r="10" fill="var(--green)"/>
          <path d="M10 4.5a3.5 3.5 0 0 0-3.5 3.5c0 2.6 3.5 7 3.5 7s3.5-4.4 3.5-7A3.5 3.5 0 0 0 10 4.5zm0 4.8a1.3 1.3 0 1 1 0-2.6 1.3 1.3 0 0 1 0 2.6z" fill="#fff"/>
        </svg>
        742 E. 9th Ave, Ste 114 Spokane, WA 99208
      </div>
      <div class="contact contact-right">
        <svg class="contact-icon" viewBox="0 0 20 20" aria-hidden="true">
          <circle cx="10" cy="10" r="10" fill="var(--green)"/>
          <circle cx="10" cy="10" r="5.5" fill="none" stroke="#fff" stroke-width="1.3"/>
          <path d="M4.5 10h11M10 4.5c-2 2.5-2 8.5 0 11M10 4.5c2 2.5 2 8.5 0 11" fill="none" stroke="#fff" stroke-width="1.1"/>
        </svg>
        www.roadcasedefenders.org
      </div>

      <div class="contact-group">
        <div class="contact">
          <svg class="contact-icon" viewBox="0 0 20 20" aria-hidden="true">
            <circle cx="10" cy="10" r="10" fill="var(--green)"/>
            <path d="M7 5l2 2.6-1.2 1.3c.7 1.5 1.8 2.6 3.3 3.3l1.3-1.2L15 13l-1.2 1.8c-4.3-.3-8-4-8.3-8.3z" fill="#fff"/>
          </svg>
          (509) TRY-CASE
        </div>
        <div class="contact">
          <svg class="contact-icon" viewBox="0 0 20 20" aria-hidden="true">
            <circle cx="10" cy="10" r="10" fill="var(--green)"/>
            <rect x="6.5" y="4.5" width="7" height="11" rx="1.2" fill="none" stroke="#fff" stroke-width="1.3"/>
            <circle cx="10" cy="13.4" r="0.8" fill="#fff"/>
          </svg>
          (509) 418-2760
        </div>
      </div>
      <div class="contact contact-right">
        <svg class="contact-icon" viewBox="0 0 20 20" aria-hidden="true">
          <circle cx="10" cy="10" r="10" fill="var(--green)"/>
          <rect x="5" y="6.5" width="10" height="7" fill="none" stroke="#fff" stroke-width="1.2"/>
          <path d="M5 6.5l5 4 5-4" fill="none" stroke="#fff" stroke-width="1.2"/>
        </svg>
        barrister@mailwove.com
      </div>
    </div>
  </div>
</body>
</html>
```